Firm Stationery Design

I need a design for stationery, including: Stationery First Page, Stationery Second Sheet, Envelope, Mailing Label for Flat Envelopes, and Business Cards

```html
<!DOCTYPE html>
<html lang="en">
<head>
<meta charset="utf-8">
<title>Harlow Legal LLC – Business Cards</title>
<link href="https://fonts.googleapis.com/css2?family=Lato:wght@400;700;900&display=swap" rel="stylesheet">
<style>
  :root {
    --bg: #2b2b2b;
    --card: #ffffff;
    --ink: #1a1a1a;
    --amber: #f5a00a;
    --band: #141414;
    --on-band: #ffffff;
  }
  * { box-sizing: border-box; margin: 0; padding: 0; }
  html, body { width: 1200px; height: 694px; overflow: hidden; }
  body {
    background: var(--bg);
    font-family: 'Lato', sans-serif;
    color: var(--ink);
    position: relative;
  }
  .card {
    position: absolute;
    top: 192px;
    width: 540px;
    height: 310px;
    background: var(--card);
    border-radius: 22px;
    overflow: hidden;
  }
  .card--front { left: 40px; }
  .card--back { left: 620px; }

  .brand {
    display: flex;
    align-items: center;
    gap: 12px;
  }
  .brand__mark {
    width: 30px;
    height: 30px;
    background: var(--amber);
    flex: none;
  }
  .brand__name {
    font-weight: 900;
    color: var(--ink);
    text-transform: uppercase;
    letter-spacing: 1px;
    line-height: 1;
    white-space: nowrap;
  }
  .card--front .brand {
    position: absolute;
    left: 0; right: 0; top: 130px;
    justify-content: center;
  }
  .card--front .brand__mark { width: 40px; height: 40px; }
  .card--front .brand__name { font-size: 38px; }

  .card--back .brand {
    position: absolute;
    right: 30px;
    top: 36px;
  }
  .card--back .brand__name { font-size: 24px; }

  .person {
    position: absolute;
    left: 34px;
    top: 112px;
  }
  .person__name {
    font-size: 27px;
    font-weight: 700;
    color: var(--amber);
    line-height: 1.1;
  }
  .person__role {
    font-size: 15px;
    margin-top: 4px;
  }
  .rule {
    position: absolute;
    left: 34px;
    right: 34px;
    top: 172px;
    height: 1.5px;
    background: var(--ink);
  }
  .contacts {
    position: absolute;
    left: 34px;
    top: 184px;
    list-style: none;
    font-size: 15px;
  }
  .contacts li {
    display: flex;
    align-items: center;
    gap: 10px;
    margin-bottom: 5px;
    white-space: nowrap;
  }
  .contacts svg { width: 16px; height: 16px; fill: var(--ink); flex: none; }
  .address {
    position: absolute;
    right: 34px;
    top: 184px;
    text-align: right;
    font-size: 14px;
    line-height: 1.35;
    font-style: normal;
    white-space: nowrap;
  }
  .footer-art {
    position: absolute;
    left: 0; bottom: 0;
    width: 540px;
    height: 56px;
  }
  .website {
    position: absolute;
    right: 30px;
    bottom: 12px;
    color: var(--on-band);
    font-size: 14px;
    letter-spacing: 0.3px;
  }
</style>
</head>
<body>

  <section class="card card--front" aria-label="Business card front">
    <div class="brand">
      <span class="brand__mark"></span>
      <span class="brand__name">Harlow Legal LLC</span>
    </div>
  </section>

  <section class="card card--back" aria-label="Business card back">
    <div class="brand">
      <span class="brand__mark"></span>
      <span class="brand__name">Harlow Legal LLC</span>
    </div>

    <div class="person">
      <p class="person__name">Daniel Brooks</p>
      <p class="person__role">Owner</p>
    </div>

    <div class="rule"></div>

    <ul class="contacts">
      <li>
        <svg viewBox="0 0 24 24" aria-hidden="true"><path d="M6.6 10.8a15 15 0 0 0 6.6 6.6l2.2-2.2a1 1 0 0 1 1-.25 11.4 11.4 0 0 0 3.6.57 1 1 0 0 1 1 1V20a1 1 0 0 1-1 1A17 17 0 0 1 3 4a1 1 0 0 1 1-1h3.5a1 1 0 0 1 1 1c0 1.250.2 2.45.57 3.57a1 1 0 0 1-.25 1z"/></svg>
        044-987 654 321
      </li>
      <li>
        <svg viewBox="0 0 24 24" aria-hidden="true"><path d="M2 5h20v14H2zm2 2v.5l8 5 8-5V7zm0 2.8V17h16V9.8l-8 5z"/></svg>
        hello@harlowlegal.com
      </li>
    </ul>

    <address class="address">
      18 Marlow Street, Suite 4<br>
      30517, Eastland
    </address>

    <svg class="footer-art" viewBox="0 0 540 56" preserveAspectRatio="none" aria-hidden="true">
      <polygon points="0,44 318,44 324,36 330,36 322,50 0,50" fill="var(--amber)"/>
      <polygon points="336,12 540,12 540,56 320,56" fill="var(--band)"/>
    </svg>
    <span class="website">www.harlowlegal.com</span>
  </section>

</body>
</html>
```